Business Card Design

I would like a new business card that incorporates the new colors and font of the attached DKM4x10.pdf file of our new sign (latte & luxurious red from Kelvane Fairbrook colors) with the logo from the old business card (file name is New2014.pdf). You can remove the phrases from the old card, and just use the contact info provided above. Please let me know if you have any questions.

Industry/Entity Type

Business

Contact Information for Business Card

Dana Kay Morrow, LLC
Real Estate Attorney
842 Larkspur Street
Fernhollow, GA 30577
(O) 555-203-4179
(C) 555-372-9051
dana@dkmlawoffice.com
dkmlawoffice.com

```html
<!DOCTYPE html>
<html lang="en">
<head>
<meta charset="utf-8">
<title>Dana Kay Morrow, LLC — Business Card</title>
<link href="https://fonts.googleapis.com/css2?family=Cabin:wght@400;600&display=swap" rel="stylesheet">
<style>
  :root {
    --backdrop: #eeeeee;
    --latte: #f3e5d9;
    --luxurious-red: #a83f45;
  }
  * { margin: 0; padding: 0; box-sizing: border-box; }
  html, body {
    width: 1200px;
    height: 1001px;
    overflow: hidden;
    background: var(--backdrop);
    font-family: "Cabin", sans-serif;
    color: var(--luxurious-red);
  }
  .business-card {
    position: absolute;
    left: 408px;
    top: 164px;
    width: 384px;
    height: 673px;
    background: var(--latte);
  }
  .brand-block {
    position: absolute;
    left: 100px;
    top: 200px;
  }
  .brand-name {
    font-size: 80px;
    font-weight: 600;
    line-height: 1;
    letter-spacing: 1px;
  }
  .firm-name {
    position: absolute;
    left: 99px;
    top: 315px;
    font-size: 19px;
    font-weight: 400;
    letter-spacing: 0.5px;
    white-space: nowrap;
  }
  .firm-name .entity {
    position: absolute;
    left: 187px;
    top: -9px;
    font-size: 10px;
    letter-spacing: 1px;
  }
  .firm-rule {
    position: absolute;
    left: 100px;
    top: 343px;
    width: 158px;
    height: 1px;
    background: var(--luxurious-red);
  }
  .practice {
    position: absolute;
    left: 100px;
    top: 352px;
    font-size: 11px;
    letter-spacing: 2.6px;
    white-space: nowrap;
  }
  .contact-list {
    position: absolute;
    left: 99px;
    top: 384px;
    list-style: none;
    font-size: 18.5px;
    line-height: 26.5px;
    letter-spacing: 0.6px;
    white-space: nowrap;
  }
  .contact-list .phone { letter-spacing: 2.4px; display: flex; align-items: center; gap: 12px; }
  .contact-list .email { letter-spacing: 0.2px; }
  .contact-list svg { width: 20px; height: 18px; flex: none; }
  .web-band {
    position: absolute;
    left: 0;
    bottom: 0;
    width: 100%;
    height: 23px;
    background: var(--luxurious-red);
    color: var(--latte);
    font-size: 13px;
    letter-spacing: 3.6px;
    text-align: center;
    line-height: 23px;
  }
</style>
</head>
<body>
  <section class="business-card">
    <div class="brand-block">
      <div class="brand-name">DKM</div>
    </div>

    <h1 class="firm-name">DANA KAY MORROW<span class="entity">LLC</span></h1>
    <div class="firm-rule"></div>
    <p class="practice">REAL ESTATE ATTORNEY</p>

    <ul class="contact-list">
      <li>842 Larkspur Street</li>
      <li>Fernhollow, GA 30577</li>
      <li class="phone">
        <svg viewBox="0 0 20 18" aria-hidden="true" fill="none" stroke="currentColor" stroke-width="1.2">
          <path d="M2 6 Q10 0 18 6 L16 8 L13 7 L13 5 Q10 4 7 5 L7 7 L4 8 Z"/>
          <rect x="5" y="9" width="10" height="7" rx="1.5"/>
          <circle cx="10" cy="12.5" r="1.8"/>
        </svg>
        555-203-4179
      </li>
      <li class="phone">
        <svg viewBox="0 0 20 18" aria-hidden="true" fill="none" stroke="currentColor" stroke-width="1.2">
          <rect x="5" y="1" width="10" height="16" rx="1.5"/>
          <line x1="5" y1="13" x2="15" y2="13"/>
          <circle cx="10" cy="15" r="0.8"/>
        </svg>
        555-372-9051
      </li>
      <li class="email">dana@dkmlawoffice.com</li>
    </ul>

    <footer class="web-band">www.dkmlawoffice.com</footer>
  </section>
</body>
</html>
```